LumenCrest Brochure Design - UPDATE/BUDGET INCREASE

Thanks everyone that have submitted designes. Please see the updates below (mostly the pricing guide and information).

UPDATE:

All images that should be used are located here: https://www.filevault-example.com/sh/kq3rtz8wmvpa1yb/Xj7pLm2Rt4

Brochure needed to showcase photography and videography prices for potential brides and couples engaged to be married. The brochure should have 5 -6 sections that shows the various wedding media service packages we offer. We will provide the information in tiers for you to lay it out creatively.

We are looking for a half-fold 11x17 that we can place inside of "swag bags" at the smaller bridal shows. Die cut options are a plus.

We need our affiliations and credentials above the LumenCrest Logo on the front of the brochure.

Our contact information is needed at the bottom on the front of the brochure to read:

"Contact us today | info@lumencrest.org | 404.816.2273"
www.lumencrestphotography.com
available worldwide

The inside should have the information containing the photography and videography prices. The outside will contain images and a logo that we will provide for you.

Lastly, we need information about our organization. Please incorporate the information located on the brochure in the dropbox folder provided above.

PRICING UPDATE:

MATINEE - $995
4 Hour Photography Service
2 Digital Enhancements on Signature Images
500 Hi-Res Images on Laser Engraved DVD
Cataloged and Sequenced by Event Sequence
Photo Release

FULL FEATURE - $1595
5 Hour Photography Service
20 - Page LayFlat PhotoBook
1 Custom Graphic Creation
5 Digital Enhancements on Signature Images
800 Hi-Res Images on Laser Engraved DVD
Photo Release

DOUBLE FEATURE - $1899
6 Hour Photography Service
1 Additional Photo Session
1 Custom Graphic Creation
1000 Hi-Res Images on Laser Engraved DVD
Photo Release

BLOCKBUSTER - $2199
7 Hour Photography Service
1 Custom Graphic Creation
1200 Hi-Res Images on Laser Engraved DVD
Photo Release

DIRECTORS CUT - $2499
8 Hour Photography Service
1 Custom Graphic Creation
10 Digital Enhancements on Signature Images
1400 Hi-Res Images on Laser Engraved DVD
Photo Release

VIDEO - BONUS REEL - $1795 (this should be a distinct section that clearly speaks video).
6 Hour Video Service
7 - 10 min Cinematic Highlight Reel
Full Ceremony Chapter optional
Royalty Free Soundtrack
Optimization for Online Upload
2 DVD's on Laser Engraved Disks
Online Hosting for 2 month

Target Market(s)

Brides and couples engaged to be married

Industry/Entity Type

Digital

Requirements
Must have
• https://www.filevault-example.com/sh/4hw82bnx7cq0ue5/MbT5yVk3Ps for images that we would like in the design.

Nice to have
• designed to take advantage of die cut printers

```html
<!DOCTYPE html>
<html lang="en">
<head>
<meta charset="UTF-8">
<title>LumenCrest Brochure – Outside Spread</title>
<link href="https://fonts.googleapis.com/css2?family=Josefin+Sans:wght@300;400;600&family=Pinyon+Script&display=swap" rel="stylesheet">
<style>
  :root {
    --stage: #4a4a4a;
    --stage-dark: #2e2e2e;
    --paper-light: #f3ece3;
    --paper-mid: #e6dacb;
    --paper-warm: #d8c8b6;
    --frame: #ffffff;
    --ink: #1e1e1e;
    --ink-soft: #333333;
    --script: rgba(120, 100, 85, .22);
    --veil-light: rgba(255, 252, 248, .55);
    --skin-light: #d9ccc0;
    --skin-mid: #b9aaa0;
    --skin-shadow: #8d7f78;
    --badge-gold: #e8c55a;
    --badge-red: #d7283a;
    --badge-teal: #2bb3a6;
    --badge-grey: #9a9a9a;
    --badge-dark: #3b3b3b;
    --badge-navy: #3c4f8c;
    --accent: #e1574c;
  }
  * { box-sizing: border-box; margin: 0; padding: 0; }
  html, body { width: 1200px; height: 832px; overflow: hidden; }
  body {
    background: linear-gradient(180deg, var(--stage) 0%, var(--stage-dark) 100%);
    font-family: "Josefin Sans", "Helvetica Neue", Arial, sans-serif;
    position: relative;
  }
  .spread {
    position: absolute;
    left: 170px;
    top: 138px;
    width: 860px;
    height: 556px;
    display: flex;
    box-shadow: 0 20px 50px rgba(0,0,0,.45);
  }
  .panel {
    position: relative;
    width: 430px;
    height: 556px;
    overflow: hidden;
  }
  .script-word {
    position: absolute;
    font-family: "Pinyon Script", cursive;
    color: var(--script);
    white-space: nowrap;
    pointer-events: none;
  }

  /* Back panel */
  .panel--back {
    background: linear-gradient(160deg, var(--paper-light) 0%, var(--paper-mid) 55%, var(--paper-warm) 100%);
  }
  .panel--back::before {
    content: "";
    position: absolute;
    inset: 0;
    background: linear-gradient(115deg, transparent 40%, var(--veil-light) 55%, transparent 70%);
  }
  .panel--back .script-word { left: 60px; top: 440px; font-size: 64px; transform: rotate(8deg); }
  .photo {
    position: absolute;
    border: 5px solid var(--frame);
    box-shadow: 0 2px 6px rgba(0,0,0,.25);
  }
  .photo--makeup   { left: 110px; top: 26px;  width: 140px; height: 88px;  background: linear-gradient(135deg, #f0f0f0, #6a6a6a 55%, #1c1c1c); }
  .photo--portrait { left: 258px; top: 26px;  width: 150px; height: 88px;  background: linear-gradient(135deg, #2a1d18, #7b5a45 50%, #1e1612); }
  .photo--team     { left: 40px;  top: 124px; width: 370px; height: 200px; background: linear-gradient(180deg, #e2ddd8 0%, #c4b8b0 42%, #5b4668 70%, #2b2430 100%); }
  .photo--couple   { left: 40px;  top: 336px; width: 175px; height: 112px; background: linear-gradient(135deg, #2f5a24, #7a9a58 50%, #e0d0b4); }
  .photo--bride    { left: 225px; top: 336px; width: 185px; height: 112px; background: linear-gradient(135deg, #5a7cc4, #a8456a 45%, #5a2a22); }

  /* Front panel */
  .panel--front {
    background: linear-gradient(180deg, var(--skin-light) 0%, var(--skin-mid) 45%, var(--skin-light) 100%);
  }
  .front-photo {
    position: absolute;
    inset: 0;
    background:
      linear-gradient(120deg, transparent 30%, var(--veil-light) 48%, rgba(255,255,255,.2) 60%, transparent 75%),
      radial-gradient(ellipse 38% 10% at 30% 47%, rgba(70,58,52,.45), transparent 75%),
      radial-gradient(ellipse 38% 10% at 80% 51%, rgba(70,58,52,.45), transparent 75%),
      radial-gradient(ellipse 90% 60% at 55% 55%, var(--skin-mid), var(--skin-shadow) 120%);
  }
  .panel--front .script-word { left: 150px; top: 0; font-size: 60px; transform: rotate(10deg); }
  .credentials {
    position: absolute;
    left: 30px;
    top: 40px;
    width: 380px;
    height: 210px;
    background: var(--frame);
    box-shadow: 0 3px 10px rgba(0,0,0,.3);
  }
  .credentials svg { display: block; }

  .brand {
    position: absolute;
    left: 40px;
    top: 358px;
    width: 370px;
  }
  .brand__name {
    display: flex;
    align-items: center;
    gap: 10px;
    font-size: 50px;
    font-weight: 300;
    letter-spacing: 1px;
    color: var(--ink);
    line-height: 1;
  }
  .brand__mark {
    width: 30px;
    height: 30px;
    border-radius: 50%;
    background: var(--accent);
    flex: none;
  }
  .brand__rule {
    height: 1px;
    background: var(--ink);
    margin: 8px 0 7px;
  }
  .brand__tagline {
    font-size: 13px;
    font-weight: 400;
    letter-spacing: 6px;
    color: var(--ink);
    text-transform: uppercase;
  }
  .contact {
    margin-top: 18px;
    font-size: 12px;
    line-height: 1.5;
    color: var(--ink-soft);
    letter-spacing: .5px;
  }
  .contact strong { font-weight: 600; color: var(--ink); }
</style>
</head>
<body>
  <main class="spread">
    <section class="panel panel--back" aria-label="Back cover">
      <span class="script-word" aria-hidden="true">Photography</span>
      <div class="photo photo--makeup" role="img" aria-label="Black and white photo of a makeup artist at work"></div>
      <div class="photo photo--portrait" role="img" aria-label="Warm-toned portrait of a woman in a studio"></div>
      <div class="photo photo--team" role="img" aria-label="Group photo of the photography team standing in a bright room"></div>
      <div class="photo photo--couple" role="img" aria-label="Wedding couple outdoors against greenery"></div>
      <div class="photo photo--bride" role="img" aria-label="Bride with henna-painted hands in red and gold"></div>
    </section>

    <section class="panel panel--front" aria-label="Front cover">
      <div class="front-photo" role="img" aria-label="Soft close-up portrait of a bride seen through a sheer veil"></div>
      <span class="script-word" aria-hidden="true">Photography</span>

      <div class="credentials" aria-label="Affiliations and credentials">
        <svg width="380" height="210" viewBox="0 0 380 210" aria-hidden="true">
          <rect x="40" y="32" width="110" height="16" fill="var(--badge-dark)"/>
          <rect x="40" y="72" width="72" height="62" fill="none" stroke="var(--badge-gold)" stroke-width="3"/>
          <rect x="200" y="28" width="52" height="56" fill="var(--badge-navy)"/>
          <rect x="262" y="52" width="110" height="34" fill="var(--badge-red)"/>
          <rect x="150" y="110" width="100" height="34" fill="var(--badge-grey)"/>
          <rect x="255" y="132" width="118" height="64" fill="var(--badge-teal)"/>
        </svg>
      </div>

      <div class="brand">
        <div class="brand__name"><span>LUMENCREST</span><span class="brand__mark"></span></div>
        <div class="brand__rule"></div>
        <div class="brand__tagline">Photography and Cinema</div>
        <div class="contact">
          Contact us today | info@lumencrest.org | 404.816.2273<br>
          www.<strong>lumencrestphotography</strong>.com<br>
          available worldwide
        </div>
      </div>
    </section>
  </main>
</body>
</html>
```